Business Card Design Project

We would like you to create business cards. The color scheme should match our website and logo. I have attached an image of a page of our website, as well as our logo. Please Please include the logo on the left with a similar faded horizontal line, and a blueprint type sketch of a house on cribbing on the right, similar to our website. We like the idea of how this looks. I have attached a third image of an actual house on cribbing (crisscrossed wooden beams). Please include cribbing in the blueprint type sketch.

The information to be included on the business cards is

(name)
214 Alder Lane
Suite 317
West Orange, NJ 07052
908.641.2093
www.brickwardliftworks.com
info@brickwardliftworks.com

This information can be spaced in any way.

I will also be posting a job for letterhead using the same design as the business cards.

If you need anything other information or I have not been clear enough, please do not hesitate to message me.

Thank you!
Updates

This design project is now open to all designers.  Please message me with any questions.  Thank you.

Industry/Entity Type

House

Requirements
Must have
• 1. Our logo
2. Blueprint type sketch of a house on wooden cribbing.
3. Color scheme to match logo and website.
4. Information provided.

```html
<!DOCTYPE html>
<html lang="en">
<head>
<meta charset="utf-8">
<title>Brickward Liftworks — Business Card</title>
<link rel="stylesheet" href="https://fonts.googleapis.com/css2?family=Source+Sans+3:wght@600;700&display=swap">
<style>
  :root {
    --page: #ffffff;
    --card: #000000;
    --white: #ffffff;
    --orange: #f7a63a;
    --orange-deep: #f7931e;
    --cyan: #7fe3f2;
    --ink: #000000;
  }
  * { margin: 0; padding: 0; box-sizing: border-box; }
  html, body {
    width: 1200px; height: 900px; overflow: hidden;
    background: var(--page);
    font-family: "Source Sans 3", "Myriad Pro", sans-serif;
  }
  .card {
    position: absolute; left: 420px; top: 152px;
    width: 355px; height: 621px;
    background: var(--card);
    text-align: center;
  }
  .brand {
    position: absolute; left: 0; right: 0; top: 160px;
    display: flex; align-items: center; justify-content: center; gap: 10px;
  }
  .brand-mark {
    width: 14px; height: 14px; background: var(--orange-deep);
  }
  .brand-name {
    color: var(--white); font-weight: 700; font-size: 30px;
    letter-spacing: 0.5px;
  }
  .services {
    position: absolute; left: 0; right: 0; top: 236px;
    color: var(--orange-deep); font-weight: 600; font-size: 12.5px;
    display: flex; align-items: center; justify-content: center; gap: 6px;
  }
  .services .dot {
    width: 8px; height: 8px; border-radius: 50%; background: var(--orange-deep);
  }
  .phone {
    position: absolute; left: 0; right: 0; top: 304px;
    color: var(--white); font-weight: 700; font-size: 28px; letter-spacing: 0.3px;
  }
  .address {
    position: absolute; left: 0; right: 0; top: 377px;
    color: var(--orange); font-weight: 600; font-size: 14.5px; line-height: 19px;
    font-style: normal;
  }
  .email {
    position: absolute; left: 0; right: 0; top: 477px;
    color: var(--orange); font-weight: 700; font-size: 16.5px;
  }
  .web-band {
    position: absolute; left: 0; top: 516px; width: 355px; height: 64px;
    background: linear-gradient(90deg, var(--orange-deep) 0%, #ffd58a 14%, #ffffff 38%, #ffffff 60%, #c9f3f9 80%, var(--cyan) 100%);
  }
  .website {
    position: absolute; left: 0; right: 0; top: 530px;
    color: var(--ink); font-weight: 700; font-size: 17.5px;
  }
</style>
</head>
<body>
  <main class="card">
    <div class="brand">
      <span class="brand-mark"></span>
      <span class="brand-name">Brickward Liftworks</span>
    </div>
    <p class="services"><span class="dot"></span>House Raising Construction Masonry<span class="dot"></span></p>
    <p class="phone">908.641.2093</p>
    <address class="address">214 Alder Lane<br>Suite 317<br>West Orange, NJ 07052</address>
    <p class="email">info@brickwardliftworks.com</p>
    <div class="web-band" role="img" aria-label="Faint blueprint sketch of a house on cribbing over an orange to blue gradient"></div>
    <p class="website">www.brickwardliftworks.com</p>
  </main>
</body>
</html>
```